Business Card Design

We are a family run drainage & groundworks company that specialise in treatment plant installation. We work for commercial & domestic property's, we have specialised knowledge & equipment for CCTV surveys, jetting blockages & repairing all types of drainage systems.

Industry/Entity Type

Business

Contact Information for Business Card

14 Larkmoor Works
Bexwell Lane
Fordingbridge
Hampshire
SP4 7JN
Tel: 01425 318207
Fax: 01425 372915
Mobile: 07862 139047
enquiries@kestrelds.co.uk
www.kestreldrainagesolutions.co.uk

Requirements
Must have
• logo, address, the right colour green.
I need the cards to also have individuals names:

Tom fairley
Neil Marston
Laura Fairley
Kate Dunmore

And also some with just the name & address on :)

```html
<!DOCTYPE html>
<html lang="en">
<head>
<meta charset="utf-8">
<title>Kestrel Drainage Solutions – Business Card Options</title>
<link rel="stylesheet" href="https://fonts.googleapis.com/css2?family=Alegreya+Sans+SC:wght@500&display=swap">
<style>
  :root {
    --page: #ffffff;
    --green: #1f9a48;
    --green-mid: #1c7a3e;
    --green-deep: #0e5a2c;
    --green-night: #0b3f20;
    --ink: #1a1a1a;
    --white: #ffffff;
    --frost: rgba(255, 255, 255, 0.62);
  }
  * { margin: 0; padding: 0; box-sizing: border-box; }
  html, body {
    width: 1200px; height: 832px; overflow: hidden;
    background: var(--page);
    font-family: "Alegreya Sans SC", "Trebuchet MS", sans-serif;
    font-weight: 500;
    color: var(--ink);
  }
  .sheet { position: relative; width: 1200px; height: 832px; }

  .card { position: absolute; overflow: hidden; background: var(--white); }
  .card--one   { left: 44px;  top: 46px;  width: 525px; height: 344px; }
  .card--two   { left: 628px; top: 46px;  width: 519px; height: 342px; }
  .card--three { left: 40px;  top: 438px; width: 527px; height: 347px; }
  .card--four  { left: 624px; top: 438px; width: 526px; height: 347px; }

  .band-top { position: absolute; left: 0; top: 0; width: 100%; height: 59px; }
  .band-photo { position: absolute; left: 0; top: 162px; width: 100%; bottom: 0; }
  .card--four .band-top { height: 60px; }
  .card--four .band-photo { top: 165px; }

  .droplets-bright {
    background: radial-gradient(ellipse at 65% 40%, #3aa062 0%, var(--green-mid) 45%, var(--green-deep) 100%);
  }
  .droplets-dark {
    background: radial-gradient(ellipse at 70% 40%, #2f8a52 0%, #1a5e34 45%, var(--green-night) 100%);
  }
  .flat-green {
    background: radial-gradient(ellipse at 60% 45%, #2a9a55 0%, var(--green-mid) 50%, var(--green-deep) 100%);
  }
  .flat-green-bar {
    background: linear-gradient(180deg, #1b6e39 0%, var(--green-deep) 100%);
  }

  .brand { position: absolute; left: 40px; top: 64px; width: 106px; text-align: center; }
  .brand__mark { display: block; width: 87px; height: 72px; margin: 0 auto; background: var(--green); }
  .brand__name {
    display: block; margin-top: 4px;
    font-size: 10.5px; line-height: 10px; letter-spacing: 1.2px;
    color: var(--ink);
  }

  .contact {
    position: absolute; right: 34px; top: 80px;
    text-align: right; list-style: none;
    color: var(--ink);
  }
  .contact li { line-height: 15px; }
  .contact .contact__phone { font-size: 12.5px; }
  .contact .contact__web { font-size: 10px; }

  .details {
    position: absolute;
    font-size: 12px; line-height: 17px; letter-spacing: 0.3px;
    color: var(--white);
  }
  .details__person { font-size: 13px; }
  .card--one .details   { left: 41px;  top: 240px; }
  .card--two .details   { left: 166px; top: 245px; }
  .card--three .details { left: 40px;  top: 245px; }
  .card--four .details  { left: 168px; top: 249px; }

  .card--three .band-full { position: absolute; inset: 0; }
  .card--three .logo-box {
    position: absolute; left: 0; top: 60px; width: 143px; height: 104px; background: var(--white);
  }
  .card--three .brand { left: 18px; top: 62px; }
  .card--three .frost-panel {
    position: absolute; left: 160px; top: 60px; width: 367px; height: 104px; background: var(--frost);
  }
  .card--three .contact { right: 33px; top: 82px; }
</style>
</head>
<body>
<main class="sheet">

  <section class="card card--one">
    <div class="band-top droplets-bright" role="img" aria-label="Green surface covered in water droplets"></div>
    <div class="brand">
      <span class="brand__mark"></span>
      <span class="brand__name">Kestrel Drainage<br>Solutions</span>
    </div>
    <ul class="contact">
      <li class="contact__phone">Tel: 01425 318207 Fax: 01425 372915</li>
      <li class="contact__phone">Mobile: 07862 139047</li>
      <li class="contact__web">enquiries@kestrelds.co.uk</li>
      <li class="contact__web">www.kestreldrainagesolutions.co.uk</li>
    </ul>
    <div class="band-photo droplets-bright" role="img" aria-label="Close-up of water droplets on a green surface"></div>
    <div class="details">
      <p class="details__person">Tom Fairley</p>
      <p class="details__address">14 Larkmoor Works Bexwell Lane<br>Fordingbridge Hampshire SP4 7JN</p>
    </div>
  </section>

  <section class="card card--two">
    <div class="band-top droplets-dark" role="img" aria-label="Dark green surface covered in water droplets"></div>
    <div class="brand">
      <span class="brand__mark"></span>
      <span class="brand__name">Kestrel Drainage<br>Solutions</span>
    </div>
    <ul class="contact">
      <li class="contact__phone">Tel: 01425 318207 Fax: 01425 372915</li>
      <li class="contact__phone">Mobile: 07862 139047</li>
      <li class="contact__web">enquiries@kestrelds.co.uk</li>
      <li class="contact__web">www.kestreldrainagesolutions.co.uk</li>
    </ul>
    <div class="band-photo droplets-dark" role="img" aria-label="Close-up of water droplets on a dark green surface"></div>
    <div class="details">
      <p class="details__person">Neil Marston</p>
      <p class="details__address">14 Larkmoor Works Bexwell Lane<br>Fordingbridge Hampshire SP4 7JN</p>
    </div>
  </section>

  <section class="card card--three">
    <div class="band-full droplets-bright" role="img" aria-label="Full-bleed close-up of water droplets on a green surface"></div>
    <div class="logo-box"></div>
    <div class="frost-panel"></div>
    <div class="brand">
      <span class="brand__mark"></span>
      <span class="brand__name">Kestrel Drainage<br>Solutions</span>
    </div>
    <ul class="contact">
      <li class="contact__phone">Tel: 01425 318207 Fax: 01425 372915</li>
      <li class="contact__phone">Mobile: 07862 139047</li>
      <li class="contact__web">enquiries@kestrelds.co.uk</li>
      <li class="contact__web">www.kestreldrainagesolutions.co.uk</li>
    </ul>
    <div class="details">
      <p class="details__person">Laura Fairley</p>
      <p class="details__address">14 Larkmoor Works Bexwell Lane<br>Fordingbridge Hampshire SP4 7JN</p>
    </div>
  </section>

  <section class="card card--four">
    <div class="band-top flat-green-bar"></div>
    <div class="brand">
      <span class="brand__mark"></span>
      <span class="brand__name">Kestrel Drainage<br>Solutions</span>
    </div>
    <ul class="contact">
      <li class="contact__phone">Tel: 01425 318207 Fax: 01425 372915</li>
      <li class="contact__phone">Mobile: 07862 139047</li>
      <li class="contact__web">enquiries@kestrelds.co.uk</li>
      <li class="contact__web">www.kestreldrainagesolutions.co.uk</li>
    </ul>
    <div class="band-photo flat-green"></div>
    <div class="details">
      <p class="details__person">Kate Dunmore</p>
      <p class="details__address">14 Larkmoor Works Bexwell Lane<br>Fordingbridge Hampshire SP4 7JN</p>
    </div>
  </section>

</main>
</body>
</html>
```